Mirela Dawn Business Card Design

I need a business card for my daughter. She has it all described in the file below. But it needs to be square in shape. http://www.mireladawn.example is her web site

Target Market(s)

18-35 year old women

Industry/Entity Type

Fashion

Contact Information for Business Card

Please look at the attached file as it has all the details.

Requirements
Must have
• Please look at the attached file as it has all the details.
Nice to have
Should not have

```html
<!DOCTYPE html>
<html lang="en">
<head>
<meta charset="utf-8">
<title>Mirela Dawn – Business Card</title>
<link href="https://fonts.googleapis.com/css2?family=Bodoni+Moda:wght@600;700&family=Dancing+Script:wght@500&family=Lato:wght@700&display=swap" rel="stylesheet">
<style>
  :root {
    --backdrop: #d9d4cc;
    --marble-dark: #050505;
    --marble-mid: #1a1712;
    --blush: #dcb4d0;
    --blush-text: #dcb2d4;
    --ink: #000000;
    --paper: #ffffff;
  }
  html, body {
    margin: 0;
    padding: 0;
    width: 900px;
    height: 1200px;
    overflow: hidden;
    background: var(--backdrop);
  }
  .canvas {
    position: relative;
    width: 900px;
    height: 1200px;
  }
  .card {
    position: absolute;
    left: 190px;
    width: 520px;
    height: 520px;
    box-shadow: 0 4px 14px rgba(0,0,0,0.35);
    overflow: hidden;
  }
  .card--front { top: 60px; }
  .card--back { top: 620px; }
  .marble {
    position: absolute;
    inset: 0;
    background:
      radial-gradient(ellipse at 20% 15%, rgba(150,125,60,0.35), transparent 45%),
      radial-gradient(ellipse at 80% 75%, rgba(120,95,40,0.3), transparent 50%),
      linear-gradient(135deg, var(--marble-dark) 0%, var(--marble-mid) 50%, var(--marble-dark) 100%);
  }
  .front-title {
    position: absolute;
    left: 0;
    right: 0;
    top: 196px;
    margin: 0;
    text-align: center;
    font-family: "Bodoni Moda", "Didot", serif;
    font-weight: 600;
    font-size: 58px;
    letter-spacing: 1px;
    line-height: 1;
    color: var(--blush-text);
    text-transform: uppercase;
    white-space: nowrap;
  }
  .front-rule {
    position: absolute;
    left: 115px;
    width: 290px;
    top: 266px;
    height: 2px;
    background: var(--paper);
  }
  .front-tagline {
    position: absolute;
    left: 0;
    right: 0;
    top: 278px;
    margin: 0;
    text-align: center;
    font-family: "Dancing Script", cursive;
    font-weight: 500;
    font-size: 30px;
    color: var(--blush-text);
  }
  .contact-panel {
    position: absolute;
    left: 22px;
    top: 22px;
    width: 476px;
    height: 476px;
    background: var(--blush);
  }
  .role-bar {
    position: absolute;
    left: 20px;
    top: 20px;
    width: 436px;
    height: 36px;
    background: var(--ink);
    color: var(--paper);
    font-family: "Dancing Script", cursive;
    font-size: 21px;
    line-height: 36px;
    text-align: center;
    white-space: nowrap;
  }
  .contact {
    position: absolute;
    left: 34px;
    display: flex;
    align-items: center;
    gap: 14px;
    font-family: "Lato", sans-serif;
    font-weight: 700;
    font-size: 17px;
    color: var(--ink);
    white-space: nowrap;
  }
  .contact--site {
    font-family: "Bodoni Moda", serif;
    font-size: 20px;
    font-weight: 700;
  }
  .badge {
    width: 38px;
    height: 38px;
    border-radius: 50%;
    background: var(--ink);
    flex: none;
    display: flex;
    align-items: center;
    justify-content: center;
  }
  .panel-rule {
    position: absolute;
    left: 20px;
    width: 436px;
    top: 318px;
    height: 3px;
    background: var(--ink);
  }
</style>
</head>
<body>
<main class="canvas">
  <section class="card card--front">
    <div class="marble" role="img" aria-label="Black marble texture with gold veins"></div>
    <h1 class="front-title">Mirela Dawn</h1>
    <div class="front-rule"></div>
    <p class="front-tagline">let s talk fashion</p>
  </section>

  <section class="card card--back">
    <div class="marble" role="img" aria-label="Black marble texture with gold veins"></div>
    <div class="contact-panel">
      <div class="role-bar">Blogger &amp; vlogger / Beauty • Fashion • Travel</div>

      <div class="contact" style="top:86px;"><span class="badge"></span>photoloop.example/mireladawnxo</div>
      <div class="contact" style="top:142px;"><span class="badge"></span>@mireladawnxo</div>
      <div class="contact" style="top:198px;"><span class="badge"></span>chirpline.example/mireladawnxo</div>
      <div class="contact" style="top:254px;">
        <span class="badge">
          <svg width="20" height="15" viewBox="0 0 22 16" aria-hidden="true">
            <rect x="1" y="1" width="20" height="14" fill="none" stroke="#fff" stroke-width="2"/>
            <polyline points="1,1 11,9 21,1" fill="none" stroke="#fff" stroke-width="2"/>
          </svg>
        </span>mirela@mireladawn.example</div>

      <div class="panel-rule"></div>

      <div class="contact contact--site" style="top:346px;"><span class="badge"></span>mireladawn.example</div>
      <div class="contact contact--site" style="top:404px;"><span class="badge"></span>vidstream.example/mireladawn</div>
    </div>
  </section>
</main>
</body>
</html>
```